K & D A/C Compressors' Business Card

Hello,

I need someone to create a new business card for my business. The name of my Business is: K & D A/C Compressors. I sell automotive air conditioning parts (a/c parts). I would like the business card to incorporate my logo, and to have an automotive feel to it. It is important that the business card feel like it is coming from an automotive parts business.

I already have a logo, which I will provide.

Thanks.
Updates

Project Deadline Extended Reason: I feel like extending the deadline until October 9, 2017, will allow for more time to design the business card. Thank you for your understanding. Added Monday, October 2, 2017

Target Market(s)

Consumers who need automotive a/c parts, and auto mechanics.

Industry/Entity Type

Automotive

Contact Information for Business Card

Business name: K & D A/C Compressors
Business Address: 48207 Southwest 36th Street, Palm Grove, Florida 33019
Telephone: 305-472-1390
Fax: To be provided once I choose your design.
Website: www.kdcoolunits.example
Email: support@kdcoolunits.example
Names: To be provided once I choose your design.

Font styles to use
Sans Serif

Colors

Designer to choose colors to be used in the design.

Requirements
Must have
• The business card must include all of the "Business Card Details" and the logo I have uploaded.

```html
<!DOCTYPE html>
<html lang="en">
<head>
<meta charset="utf-8">
<title>K &amp; D A/C Compressors – Business Card</title>
<link rel="stylesheet" href="https://fonts.googleapis.com/css2?family=Mulish:wght@400;600&display=swap">
<style>
  :root {
    --page: #ffffff;
    --card: #333333;
    --accent: #00aeef;
    --brand-grey: #a7a9ac;
    --text-grey: #b8b8b8;
    --rule: #9a9a9a;
    --photo-light: #a9a7a8;
    --photo-dark: #5e5e5e;
  }
  * { margin: 0; padding: 0; box-sizing: border-box; }
  html, body { width: 1200px; height: 968px; overflow: hidden; background: var(--page); }
  body { position: relative; font-family: "Mulish", Arial, sans-serif; }
  .artwork { position: absolute; left: 0; top: 0; }
  .brand {
    position: absolute;
    display: flex; align-items: center; gap: 10px;
    color: var(--brand-grey);
    font-weight: 400; font-size: 22px; line-height: 1.3;
  }
  .brand-mark { width: 13px; height: 13px; background: var(--accent); flex: none; }
  .brand--front { left: 310px; top: 218px; }
  .brand--back { left: 320px; top: 508px; }
  .contact {
    position: absolute; right: 335px; top: 528px;
    text-align: right; color: var(--text-grey); font-size: 14px; line-height: 17.5px;
  }
  .contact .person-name { color: var(--accent); font-size: 19px; line-height: 22px; margin-right: 5px; }
  .contact .person-role { margin-right: 5px; margin-bottom: 27px; }
  .contact .address { margin-bottom: 9px; }
  .contact-line { display: flex; justify-content: flex-end; align-items: center; gap: 6px; }
  .contact-line svg { width: 11px; height: 11px; fill: var(--accent); flex: none; }
</style>
</head>
<body>

<svg class="artwork" width="1200" height="968" viewBox="0 0 1200 968">
  <defs>
    <linearGradient id="car-tone" x1="0" y1="0" x2="1" y2="1">
      <stop offset="0" stop-color="var(--photo-dark)"/>
      <stop offset="1" stop-color="var(--photo-light)"/>
    </linearGradient>
    <linearGradient id="dash-tone" x1="0" y1="0" x2="1" y2="0">
      <stop offset="0" stop-color="#8c8c8c"/>
      <stop offset="0.5" stop-color="#c9c9c9"/>
      <stop offset="1" stop-color="#6f6f6f"/>
    </linearGradient>
  </defs>

  <g class="card-front">
    <rect x="262" y="68" width="631" height="351" fill="var(--card)"/>
    <polygon points="820,68 893,68 893,419 732,419" fill="var(--accent)"/>
    <g role="img" aria-label="Photograph of a grey sports car shown through slanted strips">
      <polygon points="550,165 610,150 583,352 536,364" fill="url(#car-tone)"/>
      <polygon points="614,127 666,113 636,385 584,356" fill="url(#car-tone)"/>
      <polygon points="668,112 717,112 686,384 636,385" fill="url(#car-tone)"/>
      <polygon points="718,142 766,128 737,391 686,384" fill="url(#car-tone)"/>
      <polygon points="768,142 839,108 839,95 868,95 868,391 737,391" fill="url(#car-tone)"/>
    </g>
  </g>

  <g class="card-back">
    <rect x="262" y="441" width="631" height="350" fill="var(--card)"/>
    <polygon points="288,594 573,594 656,791 288,791" fill="url(#dash-tone)"
             role="img" aria-label="Photograph of a car climate-control dial with A/C buttons"/>
    <polygon points="262,441 343,441 353,467 288,467 288,764 480,764 492,791 262,791" fill="var(--accent)"/>
    <line x1="508" y1="441" x2="658" y2="791" stroke="var(--rule)" stroke-width="2"/>
  </g>
</svg>

<div class="brand brand--front">
  <span class="brand-mark"></span>
  <span class="brand-name">K &amp; D<br>A/C Compressors</span>
</div>

<div class="brand brand--back">
  <span class="brand-mark"></span>
  <span class="brand-name">K &amp; D<br>A/C Compressors</span>
</div>

<div class="contact">
  <p class="person-name">YOUR NAME</p>
  <p class="person-role">Director</p>
  <p class="address">48207 Southwest 36th Street,<br>Palm Grove, Florida 33019</p>
  <p class="contact-line">001-222-4680
    <svg viewBox="0 0 12 12"><rect x="3" y="0" width="6" height="3"/><rect x="0" y="4" width="12" height="5" rx="1"/><rect x="3" y="8" width="6" height="4"/></svg></p>
  <p class="contact-line">305-472-1390
    <svg viewBox="0 0 12 12"><path d="M2.5 0.5l2 2.6-1.2 1.4c.7 1.7 2.1 3.1 3.8 3.8l1.4-1.2 2.6 2-1.3 2.3C4.8 11.2 0.8 7.2.2 1.8z"/></svg></p>
  <p class="contact-line">www.kdcoolunits.example
    <svg viewBox="0 0 12 12"><rect x="0" y="2" width="12" height="8"/><path d="M0.5 2.5l5.5 4 5.5-4" stroke="#333" stroke-width="1.2" fill="none"/></svg></p>
  <p class="contact-line">support@kdcoolunits.example
    <svg viewBox="0 0 12 12"><circle cx="6" cy="6" r="5.2" fill="none" stroke="var(--accent)" stroke-width="1.3"/><path d="M0.8 6h10.4M6 .8c-2.6 3-2.6 7.4 0 10.4M6 .8c2.6 3 2.6 7.4 0 10.4" stroke="var(--accent)" stroke-width="1" fill="none"/></svg></p>
</div>

</body>
</html>
```